November thanksgiving specials

I need a flyer mailer for this up coming thanksgiving. We are a repair and maintenance auto shop. Our slogan is "Add More Life to Your Car". We are asking for the front of the post cards catch "Wishing you a Safe and Happy Thanksgiving" sub message of "Make sure you’re prepared for the Trip!" Orange and brown is a must. The design should be worm and comforting, The specials will be posted on the back of the post card with some details. 2 Specials. Attachment shows the content I want. Bottom paragraph is not needed if you cant incorporate.

Target Market(s)

Current Customer Base

Industry/Entity Type

Automotive

Colors
f68e4e
f37122

Requirements
Must have
• Orange and brown, thanksgiving images
Nice to have
• thanksgiving cornucopia or thanksgiving turky
Should not have
• No vehicle images, child like images or overly digitized images.

```html
<!DOCTYPE html>
<html lang="en">
<head>
<meta charset="utf-8">
<title>Thanksgiving Specials Flyer</title>
<link href="https://fonts.googleapis.com/css2?family=Open+Sans:ital,wght@0,400;0,600;0,700;0,800;1,400;1,700&family=Playfair+Display:ital,wght@1,700;1,800&display=swap" rel="stylesheet">
<style>
  :root {
    --orange: #f37122;
    --orange-soft: #f68e4e;
    --brown: #5a3418;
    --brown-dark: #3b2110;
    --cream: #fdf5ec;
    --paper: #ffffff;
    --text: #4a3a30;
    --rule: #e9c9ae;
  }
  * { box-sizing: border-box; margin: 0; padding: 0; }
  html, body { width: 820px; height: 1200px; overflow: hidden; background: #f2ece6; }
  .flyer {
    position: relative; width: 820px; height: 1200px; overflow: hidden;
    background: var(--cream); font-family: "Open Sans", sans-serif; color: var(--text);
  }
  .header {
    position: absolute; left: 0; top: 0; width: 820px; height: 165px; background: var(--paper);
  }
  .brand {
    position: absolute; left: 40px; top: 40px; display: flex; align-items: center; gap: 10px;
    font-family: "Open Sans", sans-serif; font-weight: 800; font-size: 24px; line-height: 1.05;
    color: var(--brown-dark); text-transform: uppercase; width: 230px;
  }
  .brand-dot { width: 40px; height: 40px; border-radius: 50%; background: var(--orange); flex: none; }
  .greeting {
    position: absolute; left: 300px; top: 22px; width: 490px; text-align: center;
    font-family: "Playfair Display", serif; font-style: italic; font-weight: 700;
    font-size: 46px; line-height: 1.15; color: var(--orange);
  }
  .hero {
    position: absolute; left: 0; top: 165px; width: 820px; height: 295px;
    background: radial-gradient(ellipse at 50% 75%, #c77a36 0%, #9a5222 35%, #5c3015 70%, #3a1e0d 100%);
  }
  .hero-tagline {
    position: absolute; left: 0; top: 222px; width: 820px; text-align: center;
    font-weight: 800; font-size: 36px; line-height: 1.1; color: #fff; text-transform: uppercase;
    text-shadow: 0 2px 6px rgba(0,0,0,.55);
  }
  .letter { position: absolute; left: 55px; top: 474px; width: 715px; }
  .salutation { font-weight: 700; font-size: 22px; color: var(--orange); margin-bottom: 6px; }
  .letter p { font-size: 13.5px; line-height: 1.5; }
  .letter .cta { color: var(--orange); font-weight: 700; font-size: 15px; margin-top: 4px; line-height: 1.4; }
  .specials-title {
    position: absolute; left: 55px; top: 630px; width: 715px; display: flex; align-items: center; gap: 18px;
    font-family: "Playfair Display", serif; font-style: italic; font-weight: 800; font-size: 36px; color: var(--orange);
  }
  .specials-title::before, .specials-title::after { content: ""; flex: 1; height: 2px; background: var(--rule); }
  .offer {
    position: absolute; top: 692px; height: 280px; background: var(--paper);
    border: 2px dashed var(--orange-soft);
  }
  .offer-service { left: 55px; width: 340px; padding: 16px 18px; }
  .service-list { list-style: none; font-size: 13px; line-height: 1.35; }
  .service-list li { display: flex; gap: 8px; margin-bottom: 4px; }
  .service-list svg { flex: none; margin-top: 2px; }
  .price-tag {
    position: absolute; left: 18px; right: 18px; bottom: 14px; text-align: center;
    background: var(--orange); color: #fff; padding: 6px 0;
  }
  .price-tag strong { display: block; font-size: 24px; font-weight: 800; line-height: 1.1; }
  .price-tag span { font-size: 11px; }
  .offer-gift { left: 425px; width: 345px; padding: 18px 20px; text-align: center; }
  .gift-kicker { font-weight: 700; font-size: 17px; color: var(--orange); }
  .gift-title { font-weight: 400; font-size: 30px; color: var(--brown); letter-spacing: 1px; margin: 2px 0 10px; }
  .gift-body { font-size: 12.5px; line-height: 1.45; text-transform: uppercase; font-weight: 600; }
  .gift-shop { margin-top: 6px; font-size: 13px; line-height: 1.4; }
  .gift-phone { font-weight: 800; font-size: 24px; color: var(--brown); margin: 4px 0; }
  .gift-fine { font-size: 10px; font-style: italic; line-height: 1.35; }
  .closing { position: absolute; left: 55px; top: 984px; width: 715px; font-size: 12.5px; line-height: 1.45; }
  .footer {
    position: absolute; left: 0; top: 1062px; width: 820px; height: 138px;
    background: linear-gradient(90deg, var(--orange) 0%, var(--orange-soft) 100%);
  }
  .signoff { position: absolute; left: 55px; top: 1082px; color: #fff; }
  .signoff em { font-size: 15px; }
  .signoff strong { display: block; font-size: 17px; font-weight: 800; margin-top: 2px; }
  .signoff span { display: block; font-size: 11px; line-height: 1.45; }
  .cornucopia {
    position: absolute; left: 560px; top: 1070px; width: 240px; height: 124px; border-radius: 50%;
    background: radial-gradient(ellipse at 45% 55%, #e9a043 0%, #c86a24 45%, #8a4b1c 75%, rgba(138,75,28,0) 100%);
  }
</style>
</head>
<body>
<main class="flyer">
  <header class="header">
    <div class="brand"><span class="brand-dot"></span>Keystone Auto Care</div>
    <h1 class="greeting">Wishing you a Safe and Happy Thanksgiving!!</h1>
  </header>

  <div class="hero" role="img" aria-label="Roast turkey Thanksgiving dinner table with autumn decorations"></div>
  <h2 class="hero-tagline">Make sure you're prepared<br>for the trip!</h2>

  <section class="letter">
    <div class="salutation">Dear Friends,</div>
    <p>Yes, it is almost time to go back Grandma's for the Thanksgiving! Let us help take one worry out of this time of year and give you peace of mind with your vehicle while you travel. Take advantage of these Specials to help get ready for the holidays.</p>
    <p class="cta">Vehicles must be dropped off!<br>Make an appointment come in by November 31, 2015 and we will perform our:</p>
  </section>

  <h2 class="specials-title">"Thanksgiving Specials"</h2>

  <section class="offer offer-service">
    <ul class="service-list">
      <li><svg width="13" height="13" viewBox="0 0 13 13"><rect x="0.5" y="0.5" width="12" height="12" fill="none" stroke="#f37122"/><path d="M3 6.5l2.5 2.5L10 3.5" fill="none" stroke="#f37122" stroke-width="2"/></svg>Full Synthetic Oil, Filter &amp; Lube Service up to 5 quarts of oil</li>
      <li><svg width="13" height="13" viewBox="0 0 13 13"><rect x="0.5" y="0.5" width="12" height="12" fill="none" stroke="#f37122"/><path d="M3 6.5l2.5 2.5L10 3.5" fill="none" stroke="#f37122" stroke-width="2"/></svg>23 Point Maintenance Inspection</li>
      <li><svg width="13" height="13" viewBox="0 0 13 13"><rect x="0.5" y="0.5" width="12" height="12" fill="none" stroke="#f37122"/><path d="M3 6.5l2.5 2.5L10 3.5" fill="none" stroke="#f37122" stroke-width="2"/></svg>Complete Brake Inspection</li>
      <li><svg width="13" height="13" viewBox="0 0 13 13"><rect x="0.5" y="0.5" width="12" height="12" fill="none" stroke="#f37122"/><path d="M3 6.5l2.5 2.5L10 3.5" fill="none" stroke="#f37122" stroke-width="2"/></svg>Tire Rotation as Needed</li>
      <li><svg width="13" height="13" viewBox="0 0 13 13"><rect x="0.5" y="0.5" width="12" height="12" fill="none" stroke="#f37122"/><path d="M3 6.5l2.5 2.5L10 3.5" fill="none" stroke="#f37122" stroke-width="2"/></svg>Inspect Belts and Hoses</li>
      <li><svg width="13" height="13" viewBox="0 0 13 13"><rect x="0.5" y="0.5" width="12" height="12" fill="none" stroke="#f37122"/><path d="M3 6.5l2.5 2.5L10 3.5" fill="none" stroke="#f37122" stroke-width="2"/></svg>Top Off All Fluids</li>
      <li><svg width="13" height="13" viewBox="0 0 13 13"><rect x="0.5" y="0.5" width="12" height="12" fill="none" stroke="#f37122"/><path d="M3 6.5l2.5 2.5L10 3.5" fill="none" stroke="#f37122" stroke-width="2"/></svg>Consultation on Any Problems With Your Vehicle</li>
    </ul>
    <div class="price-tag"><strong>$25 OFF</strong><span>(A $35 value for most vehicles)</span></div>
  </section>

  <section class="offer offer-gift">
    <div class="gift-kicker">20% off Brake Special</div>
    <div class="gift-title">GIFT CERTIFICATE</div>
    <div class="gift-body">Worth $20 towards your next brake service over $150</div>
    <div class="gift-shop">at Keystone Auto Care<br>4820 Harvest Lane<br>Maple Grove, CA 90412</div>
    <div class="gift-phone">310-555-0186</div>
    <div class="gift-fine">(No charge required, not good with any other offer)<br>Expires December 15th</div>
  </section>

  <p class="closing">If you have any family or friends who could also benefit from one of the "Thanksgiving SPECIALS" above, have them call us by November 31, and mention your name. We will extend this offer to them as an additional courtesy to you. This is just another way of saying THANK YOU for your trust and loyalty and for stopping by before the colder months. We look forward to seeing you soon!</p>

  <footer class="footer"></footer>
  <div class="signoff">
    <em>Sincerely,</em>
    <strong>Marco &amp; Daniel, Owners</strong>
    <span>Keystone Auto Care · 4820 Harvest Lane, Maple Grove, CA 90412<br>Phone 310-555-0186</span>
  </div>
  <div class="cornucopia" role="img" aria-label="Cornucopia overflowing with autumn fruits, squash and leaves"></div>
</main>
</body>
</html>
```